Classy business card for accounting firm

We're looking for a new business card for our accounting firm. Our logo was designed by Brandolith, so all of the design info we would like to use has been provided. The specific font provided isn't required to be used.

We want the card to look classy and elegent. Probably more minimalistic, but still with some pops of color.

The options we would like to include on the card are as follows:
1. Main office phone line
2. Direct phone line
3. Email address
4. Website URL
5. Name
6. Title (CEO, President, etc.)
7. Firm Address

The design and card should be double sided!!! The drop down box in the project brief for some reason is defaulting to single sided. Not sure why this is happening.

Thanks!

Contact Information for Business Card

The options we would like to include on the card are as follows: 1. Main office phone line 2. Direct phone line 3. Email address 4. Website URL 5. Name 6. Title (CEO, President, etc.) 7. Firm Address

Requirements
Must have
• Card must be double sided.

```html
<!DOCTYPE html>
<html lang="en">
<head>
<meta charset="utf-8">
<title>Cedarline Partners – Business Card</title>
<link href="https://fonts.googleapis.com/css2?family=Montserrat:wght@400;500;600&display=swap" rel="stylesheet">
<style>
  :root {
    --stage: #1f1f1f;
    --card-front: #5e5e5e;
    --card-front-light: #7a7a7a;
    --card-back: #ffffff;
    --ink: #575757;
    --ink-soft: #6a6a6a;
    --lime: #a9bb24;
    --orange: #e8731a;
    --navy: #3c4250;
    --white: #ffffff;
  }
  * { margin: 0; padding: 0; box-sizing: border-box; }
  html, body { width: 900px; height: 1200px; overflow: hidden; }
  body {
    background: var(--stage);
    font-family: "Montserrat", sans-serif;
    position: relative;
  }
  .card {
    position: absolute;
    left: 187px;
    width: 526px;
    height: 298px;
    overflow: hidden;
  }
  .card-front { top: 274px; background: var(--card-front); }
  .card-back { top: 604px; background: var(--card-back); }

  .front-pattern {
    position: absolute; inset: 0;
    background: linear-gradient(90deg, #555555 0%, #5f5f5f 55%, var(--card-front-light) 100%);
  }
  .front-brand {
    position: absolute;
    left: 89px; top: 128px;
    display: flex; align-items: center; gap: 18px;
  }
  .brand-square { width: 32px; height: 32px; background: var(--orange); flex: none; }
  .front-brand .brand-name {
    color: var(--white);
    font-size: 19px; font-weight: 500; letter-spacing: 1.3px;
    line-height: 1; white-space: nowrap;
  }
  .tagline {
    display: flex; align-items: center; gap: 8px;
    font-size: 9px; letter-spacing: 1.6px; font-weight: 500;
    margin-top: 8px; white-space: nowrap;
  }
  .tagline::before, .tagline::after {
    content: ""; flex: 1; height: 1px; background: var(--lime);
  }
  .front-brand .tagline { color: var(--white); }

  .back-brand {
    position: absolute;
    left: 36px; top: 106px; width: 210px;
    text-align: center;
  }
  .back-brand .brand-square { width: 32px; height: 32px; margin: 0 auto 34px; }
  .back-brand .brand-name {
    color: var(--ink);
    font-size: 16px; font-weight: 600; letter-spacing: 0.5px; line-height: 1;
    white-space: nowrap;
  }
  .back-brand .tagline { color: var(--ink); font-size: 8px; font-weight: 600; margin-top: 6px; letter-spacing: 1.2px; }

  .divider {
    position: absolute; left: 263px; top: 73px;
    width: 1px; height: 153px; background: var(--navy);
  }
  .divider-accent {
    position: absolute; left: 262px; top: 98px;
    width: 3px; height: 105px; background: var(--lime);
  }
  .contact {
    position: absolute; left: 282px; top: 70px;
    color: var(--ink-soft);
  }
  .contact-name { font-size: 16px; font-weight: 600; color: var(--ink); letter-spacing: 0.3px; }
  .contact-title { font-size: 12.5px; color: var(--lime); margin-top: 3px; letter-spacing: 0.3px; }
  .contact-address { font-size: 12.5px; line-height: 17px; margin-top: 7px; letter-spacing: 0.6px; }
  .contact-list { list-style: none; margin-top: 10px; font-size: 12.5px; letter-spacing: 0.6px; }
  .contact-list li { display: flex; align-items: center; gap: 6px; height: 18.7px; }
  .contact-list svg { width: 11px; height: 11px; flex: none; }

  .corner-accent {
    position: absolute; left: 448px; top: 175px; width: 78px; height: 123px;
    background: linear-gradient(180deg, #f1f4e2 0%, #f3efe2 40%, #fde9dc 100%);
  }
</style>
</head>
<body>
  <section class="card card-front" aria-label="Card front">
    <div class="front-pattern" role="img" aria-label="Embossed repeating pattern in graphite tones"></div>
    <div class="front-brand">
      <span class="brand-square"></span>
      <div>
        <div class="brand-name">CEDARLINE PARTNERS</div>
        <div class="tagline">TRUSTED TAX GUIDANCE</div>
      </div>
    </div>
  </section>

  <section class="card card-back" aria-label="Card back">
    <div class="back-brand">
      <div class="brand-square"></div>
      <div class="brand-name">CEDARLINE PARTNERS</div>
      <div class="tagline">TRUSTED TAX GUIDANCE</div>
    </div>

    <div class="divider"></div>
    <div class="divider-accent"></div>

    <div class="contact">
      <div class="contact-name">MARTIN CALLOWAY, EA</div>
      <div class="contact-title">CEO &amp; President</div>
      <div class="contact-address">410 W. Alder St<br>Portland, OR 97205</div>
      <ul class="contact-list">
        <li>
          <svg viewBox="0 0 12 12" aria-hidden="true"><rect x="1" y="4" width="10" height="7" rx="1" fill="var(--orange)"/><path d="M1 4 Q6 0 11 4" stroke="var(--orange)" stroke-width="1.6" fill="none"/><circle cx="6" cy="7.5" r="1.6" fill="#fff"/></svg>
          503-555-0142
        </li>
        <li>
          <svg viewBox="0 0 12 12" aria-hidden="true"><path d="M2.5 1 L4.5 1 L5.5 3.8 L4.2 4.8 Q5.2 7 7.2 7.8 L8.2 6.5 L11 7.5 L11 9.5 Q10.5 11 9 11 Q1 10 1 2.5 Q1 1 2.5 1 Z" fill="var(--orange)"/></svg>
          503-555-0187
        </li>
        <li>
          <svg viewBox="0 0 12 12" aria-hidden="true"><rect x="1" y="2.5" width="10" height="7" fill="var(--orange)"/><path d="M1 2.5 L6 6.5 L11 2.5" stroke="#fff" stroke-width="1" fill="none"/></svg>
          info@cedarline.cc
        </li>
        <li>
          <svg viewBox="0 0 12 12" aria-hidden="true"><circle cx="6" cy="6" r="4.8" stroke="var(--orange)" stroke-width="1" fill="none"/><ellipse cx="6" cy="6" rx="2" ry="4.8" stroke="var(--orange)" stroke-width="1" fill="none"/><path d="M1.2 6 H10.8 M2 3.5 H10 M2 8.5 H10" stroke="var(--orange)" stroke-width="0.8"/></svg>
          www.cedarline.cc
        </li>
      </ul>
    </div>

    <div class="corner-accent" role="img" aria-label="Faint oversized watermark shape in pale lime and peach"></div>
  </section>
</body>
</html>
```